Cover page for Master's thesis (in Word)

I need a cover page for my Master's thesis which I am currently working on. The topic is "Mobile Usability" so MOBILE should also be the overall theme of the design. The primary color should be blue since my school and the company where I am writing my thesis are primarily using blue in their Corporate Identities.
I enclosed a template in Word and pdf with all the necessary information that must be included on the cover page. Please also consider and adhere to the page margins and the printable areas set in the Word template and please use Verdana for the mandatory text elements mentioned. The topic font can be different and it's up to you.
The design shouldn't be too fancy since this is a dissertation and not an ad for an Quince product. I would prefer a simple, flat, modern and professional design with flat colors. I also attached the logo of my University and my company (which should of course be included) as well as a leaflet of my Uni for inspiration.

If you have any questions or if you need more information or material, just drop me a line.

Thanks a lot in advance!
Torben

```html
<!DOCTYPE html>
<html lang="en">
<head>
<meta charset="utf-8">
<title>Master's thesis – Mobile Usability</title>
<link rel="stylesheet" href="https://fonts.googleapis.com/css2?family=Baloo+2:wght@800&display=swap">
<style>
  :root {
    --page: #ffffff;
    --ink: #111111;
    --brand-blue: #1768b3;
    --title-blue: #1a6cb5;
    --rule-blue: #3f7fbf;
    --globe-light: #49b1ea;
    --globe-dark: #1489d6;
  }
  html, body { margin: 0; padding: 0; overflow: hidden; background: var(--page); }
  .cover {
    position: relative;
    width: 848px; height: 1200px;
    background: var(--page);
    font-family: Verdana, "DejaVu Sans", sans-serif;
    color: var(--ink);
    overflow: hidden;
  }
  .school-name {
    position: absolute; left: 91px; top: 66px; width: 210px;
    font-size: 18px; line-height: 22px; color: var(--brand-blue);
    font-weight: 700;
  }
  .school-name .mark {
    display: inline-block; width: 12px; height: 12px;
    background: var(--brand-blue); margin-right: 8px; vertical-align: 1px;
  }
  .company-name {
    position: absolute; left: 470px; top: 76px; width: 270px;
    font-size: 32px; line-height: 40px; font-weight: 700;
    color: var(--brand-blue); letter-spacing: 1px;
  }
  .company-name .dot {
    display: inline-block; width: 20px; height: 20px; border-radius: 50%;
    background: var(--brand-blue); margin-left: 12px; vertical-align: 2px;
  }
  .rule { position: absolute; height: 1px; background: var(--rule-blue); }
  .rule--header { left: 80px; width: 674px; top: 165px; }
  .rule--title { left: 66px; width: 707px; top: 360px; }
  .doc-type {
    position: absolute; left: 0; right: 0; top: 203px;
    text-align: center; font-size: 21px; font-weight: 700;
  }
  .thesis-title {
    position: absolute; left: 0; right: 0; top: 280px;
    text-align: center; margin: 0;
    font-family: "Baloo 2", "Arial Rounded MT Bold", sans-serif;
    font-weight: 800; font-size: 60px; line-height: 70px;
    color: var(--title-blue);
  }
  .thesis-subtitle {
    position: absolute; left: 0; right: 0; top: 402px;
    text-align: center; margin: 0;
    font-family: "Baloo 2", "Arial Rounded MT Bold", sans-serif;
    font-weight: 800; font-size: 27px; line-height: 41px;
    color: var(--title-blue);
  }
  .globe {
    position: absolute; left: 214px; top: 497px;
    width: 392px; height: 380px; border-radius: 50%;
    background: radial-gradient(circle at 40% 35%, var(--globe-light), var(--globe-dark));
  }
  .details {
    position: absolute; left: 73px; top: 916px;
    border-collapse: collapse; font-size: 14.5px;
  }
  .details th {
    text-align: left; font-weight: 700; width: 252px;
    padding: 0; height: 34.7px;
  }
  .details td { padding: 0; }
</style>
</head>
<body>
<main class="cover">
  <div class="school-name"><span class="mark"></span>Hochschule Auerbach Business School</div>
  <div class="company-name">LOYALTO<span class="dot"></span></div>
  <div class="rule rule--header"></div>

  <div class="doc-type">Master’s thesis</div>
  <h1 class="thesis-title">Mobile Usability</h1>
  <div class="rule rule--title"></div>
  <h2 class="thesis-subtitle">Analysis of the mobile application portfolio of<br>XXXXX Ltd.</h2>

  <div class="globe" role="img" aria-label="Blue globe showing Europe and Africa with small red mobile phone markers across the map"></div>

  <table class="details">
    <tr><th>Surname, Name</th><td>Torben Hallmann</td></tr>
    <tr><th>Matriculation Number</th><td>000XXXXX</td></tr>
    <tr><th>Degree Program</th><td>Marketing / Sales / Media</td></tr>
    <tr><th>Issued on</th><td>06.11.2013</td></tr>
    <tr><th>Submitted on</th><td>07.04.2014</td></tr>
    <tr><th>First Examiner</th><td>Prof. Dr. Marta Kessel</td></tr>
    <tr><th>Second Examiner</th><td>Prof. Dr. Jonas Brehm</td></tr>
  </table>
</main>
</body>
</html>
```